Tolnar Social Media Banner

The objective of this campaign is to end up with a Banner Add to post in the content of our social media.

We are Tolnar, a business that is going to modify all the grocery shopping mechanism with a simple device. It works the following way. Our device is a bar-code scanner. Once installed in your home, you would scan your groceries trough and it will automatically create your shopping list. Once you decide you have all the items, you just click the “buy” button and you’ll receive your groceries home whenever you have selected. This way is like being in the grocery shop but from home. You’ll find a long video and short video attached to the project.

The objective is to create a Banner Add that simulates the SHORT video with icons. The goal is for the viewer to understand what our device do just by looking at the banner. We have thought about diving the banner into three frames: Scan, Buy and Receive. Although that is what we think is most understandable, let us know if you think otherwise.

For the Scan frame the viewer should be able to see clearly the scanning process of any grocery through our device. I attached a picture of how our device looks like. You could also look for more images googling “Tolnar”.

For the Buy frame there should be a mobile phone. The idea is that the viewer is able to recognize that the Buying process is through an App in your phone. The frame could be only a phone, it could also be a phone with the Tolnar app opened or even a phone with a “Buy” button. Further ideas for this icon will be more than welcome.

The Receive frame should be the easiest one of them all. It should be more than clear the meaning of the frame.

Between the frames, you could add some to enable to understand the whole process. There could be numbers (Example: 1. Scan, 2. Buy, 3. Receive), there could be a plus sign (Example: Scan + Buy = Receive), or there could also be arrows following the process. Again, ideas to this matter will be more than welcome.

Thank you and contact us for questions or more info.

- Long video: https://www.vidmarsh.example/watch?v=Qa7rLmPzE2d

- Short Video: https://www.vidmarsh.example/watch?v=Hn3xBtYcW9k

- Tolnar Device Picture: https://www.findlo.example/search?q=tolnar&img=1#r=Pq4sTz8wLm2A

- Tolnar Logo: https://www.findlo.example/search?q=tolnar&img=1#r=Vd6kGh1nRs9B

- Tolnar App: https://www.findlo.example/search?q=tolnar+app&img=1#r=Jw2cYe5uXo7C

Industry/Entity Type

Business

Requirements
Must have
• Hi again. I just uploaded an example of what we are looking for. Open the file Tolnar_Expositor. We would like the designs to adjust to it. Although that's what we would like, we are open to new propositions.
• IMPORTANT:
• 1. We would like to change where it says scan. I've uploaded a picture called Captura. The idea is to draw the device SCANNING a product so that it is clear the function of the scan.
• 2. Dimensions of the composition. We would like more room for the Scan, Check and Receive compositions. That is going to be done reducing the blue space.
• 3. Bottom of the image. As you will see there is a pretty big grey space at the bottom of the image. The idea is to reduce it a little bit. The corner of the white line should be pretty close to the end of the image, or even touching.

```html
<!DOCTYPE html>
<html lang="en">
<head>
<meta charset="utf-8">
<title>Tolnar – grocery shopping banner</title>
<link rel="stylesheet" href="https://fonts.googleapis.com/css2?family=Encode+Sans+Condensed:wght@300;400;600&display=swap">
<style>
  :root {
    --sun: #fdc113;
    --sun-light: #fed556;
    --paper: #ffffff;
    --ink: #4a4a4a;
    --ink-soft: #3a3a3a;
    --scan-blue: #3ba6dd;
    --check-green: #8dc63f;
    --receive-red: #f05a2a;
    --device-light: #e6e0d6;
    --device-shade: #c9c1b4;
    --bag-blue: #2e9fdc;
    --bag-green: #8cc63f;
    --bag-orange: #e85a30;
  }
  html, body {
    margin: 0;
    padding: 0;
    overflow: hidden;
    background: var(--paper);
  }
  .banner {
    position: relative;
    width: 1200px;
    height: 400px;
    overflow: hidden;
    background: var(--sun);
    font-family: "Encode Sans Condensed", "Arial Narrow", sans-serif;
  }
  .backdrop {
    position: absolute;
    inset: 0;
  }
  .bag-art {
    position: absolute;
    left: 222px;
    top: 70px;
    width: 168px;
    height: 168px;
    transform: rotate(-8deg);
    border: 6px solid var(--paper);
    border-radius: 4px;
    background: linear-gradient(90deg, var(--bag-blue) 0%, var(--bag-green) 45%, var(--bag-green) 70%, var(--bag-orange) 100%);
  }
  .headline {
    position: absolute;
    right: 450px;
    top: 68px;
    margin: 0;
    color: var(--paper);
    font-weight: 300;
    font-size: 44px;
    line-height: 50px;
    text-align: right;
    white-space: nowrap;
  }
  .headline .brand-inline {
    font-weight: 600;
    font-size: 50px;
    margin-right: 6px;
  }
  .device-art {
    position: absolute;
    left: 744px;
    top: 66px;
    width: 162px;
    height: 308px;
    clip-path: polygon(28px 0, 100% 0, 100% 100%, 0 100%, 0 82%, 20px 50%, 28px 30%);
    background: linear-gradient(160deg, var(--device-light) 0%, var(--device-light) 55%, var(--device-shade) 100%);
  }
  .step {
    position: absolute;
    display: flex;
    flex-direction: column;
    align-items: center;
    justify-content: flex-end;
    color: var(--paper);
    border-radius: 8px;
    padding-bottom: 6px;
    box-sizing: border-box;
    font-weight: 400;
  }
  .step svg { margin-bottom: 4px; }
  .step--scan { left: 936px; top: 56px; width: 100px; height: 104px; background: var(--scan-blue); font-size: 19px; }
  .step--check { left: 932px; top: 186px; width: 88px; height: 88px; background: var(--check-green); font-size: 19px; }
  .step--receive { left: 914px; top: 292px; width: 78px; height: 78px; background: var(--receive-red); font-size: 19px; font-weight: 600; }
  .step-tail { position: absolute; }
  .brand-block {
    position: absolute;
    left: 112px;
    top: 300px;
    display: flex;
    align-items: center;
  }
  .brand-name {
    color: var(--ink);
    font-weight: 600;
    font-size: 76px;
    line-height: 1;
    width: 200px;
  }
  .divider {
    width: 1px;
    height: 80px;
    background: var(--ink-soft);
    margin: 0 26px 0 18px;
  }
  .contact {
    list-style: none;
    margin: 0;
    padding: 0;
    color: var(--ink-soft);
    font-size: 21px;
  }
  .contact li {
    display: flex;
    align-items: center;
    gap: 14px;
    height: 32px;
  }
</style>
</head>
<body>
<main class="banner">
  <svg class="backdrop" width="1200" height="400" viewBox="0 0 1200 400" aria-hidden="true">
    <polygon points="0,116 1032,344 0,172" fill="var(--sun-light)"/>
    <polygon points="0,172 1032,344 1200,184 1200,400 0,400" fill="var(--paper)"/>
  </svg>

  <div class="bag-art" role="img" aria-label="Shopping bag illustration in blue, green and orange stripes"></div>

  <h1 class="headline">
    <span class="brand-inline">tolnar</span>does your<br>grocery shopping<br>for you
  </h1>

  <div class="device-art" role="img" aria-label="Photo of the Tolnar home scanner device"></div>

  <svg class="step-tail" style="left:926px;top:142px" width="16" height="16" viewBox="0 0 16 16" aria-hidden="true"><polygon points="10,0 16,0 16,10 0,16" fill="var(--scan-blue)"/></svg>
  <div class="step step--scan">
    <svg width="46" height="46" viewBox="0 0 46 46" aria-hidden="true">
      <rect x="14" y="4" width="22" height="34" rx="3" fill="none" stroke="#fff" stroke-width="2"/>
      <circle cx="25" cy="17" r="6" fill="none" stroke="#fff" stroke-width="2"/>
      <line x1="4" y1="30" x2="20" y2="22" stroke="#fff" stroke-width="2"/>
    </svg>
    <span>Scan</span>
  </div>

  <svg class="step-tail" style="left:922px;top:184px" width="16" height="16" viewBox="0 0 16 16" aria-hidden="true"><polygon points="0,0 16,4 16,14 10,14" fill="var(--check-green)"/></svg>
  <div class="step step--check">
    <svg width="24" height="40" viewBox="0 0 24 40" aria-hidden="true">
      <rect x="1" y="1" width="22" height="38" rx="3" fill="#fff"/>
      <rect x="3" y="6" width="18" height="26" fill="var(--check-green)" opacity="0.35"/>
      <circle cx="12" cy="19" r="4" fill="var(--check-green)"/>
      <circle cx="12" cy="35" r="1.6" fill="var(--check-green)"/>
    </svg>
    <span>Check</span>
  </div>

  <svg class="step-tail" style="left:902px;top:290px" width="16" height="20" viewBox="0 0 16 20" aria-hidden="true"><polygon points="0,0 16,4 16,20 10,20" fill="#f58b2a"/></svg>
  <div class="step step--receive">
    <svg width="30" height="30" viewBox="0 0 30 30" aria-hidden="true">
      <polygon points="15,3 27,9 15,15 3,9" fill="#fff"/>
      <polygon points="3,9 15,15 15,28 3,22" fill="#f3f3f3"/>
      <polygon points="27,9 15,15 15,28 27,22" fill="#e0e0e0"/>
      <polygon points="9,6 21,12 21,16 9,10" fill="#d9d9d9"/>
    </svg>
    <span>Receive</span>
  </div>

  <footer class="brand-block">
    <div class="brand-name">tolnar</div>
    <div class="divider"></div>
    <ul class="contact">
      <li>
        <svg width="20" height="20" viewBox="0 0 20 20" aria-hidden="true">
          <path d="M4 2 L7 2 L8.5 6 L6.5 7.5 Q8 11.5 12.5 13.5 L14 11.5 L18 13 L18 16 Q17 18 15 18 Q4 16 2 5 Q2 3 4 2 Z" fill="var(--check-green)"/>
        </svg>
        <span>+00 111 222 3344</span>
      </li>
      <li>
        <svg width="22" height="16" viewBox="0 0 22 16" aria-hidden="true">
          <rect x="1" y="1" width="20" height="14" fill="none" stroke="var(--check-green)" stroke-width="2"/>
          <polyline points="1,1 11,9 21,1" fill="none" stroke="var(--check-green)" stroke-width="2"/>
        </svg>
        <span>hello@tolnar-home.example</span>
      </li>
    </ul>
  </footer>
</main>
</body>
</html>
```